Corporate Intelligence Agency seeks redesign *

Varnholt Insight is a business intelligence firm made up of former special operations and intelligence professionals. Our vibe is quiet professionals that get the job done by whatever means necessary.
Our aesthetic is clean, sleek, and monochromatic. We prefer the texture contrasts over colors. Slick white or black, playing up textures, and bold block lettering, and simplicity are what we are looking for in a design.

The logo would preferably pay homage to our military/special operations roots, and the culture of changing for the better (alchemy) that we embody all while remaining simple.

Target Market(s)

C-Level executives with a taste for the simple over the extravagant, and cut right to the chase

Industry/Entity Type

Management Solution

Contact Information for Business Card

Back is matte black with a glossy black logo to contrast. The front has the logo, with space on the bottom left for name and contact

Logo Text

Varnholt Ins.

Logo styles of interest
Abstract Logo
Wordmark Logo
Lettermark Logo
Font styles to use
Serif
Sans Serif
Script

Requirements
Must have
• Monochromatic, play on texture within card (the card ought to be memorable to hold), solid/clean lettering. Logo should be simple and sleek.
Nice to have
• If the logo can tie alchemy and intelligence/spy genre. 3d textures
Should not have
• Nothing overtly military. No colors outside of the monochromatic spectrum

```html
<!DOCTYPE html>
<html lang="en">
<head>
<meta charset="utf-8">
<title>Varnholt Insight — Business Card</title>
<link rel="stylesheet" href="https://fonts.googleapis.com/css2?family=EB+Garamond:wght@400;500&family=Exo+2:ital,wght@1,800&display=swap">
<style>
  :root {
    --stage: #d4d4d4;
    --card-light: #f0f0f0;
    --card-light-edge: #e4e4e4;
    --card-dark: #2b2929;
    --card-dark-sheen: #3b3939;
    --ink: #2a2a2a;
    --ink-soft: #3a3a3a;
    --paper: #ffffff;
  }
  * { margin: 0; padding: 0; box-sizing: border-box; }
  html, body {
    width: 1200px;
    height: 800px;
    overflow: hidden;
    background: var(--stage);
  }
  .stage {
    position: relative;
    width: 1200px;
    height: 800px;
  }
  .card {
    position: absolute;
    top: 272px;
    width: 402px;
    height: 262px;
  }
  .card--front {
    left: 134px;
    background: linear-gradient(120deg, var(--paper) 0%, var(--card-light) 55%, var(--card-light-edge) 100%);
    color: var(--ink);
  }
  .card--back {
    left: 636px;
    background: linear-gradient(100deg, var(--card-dark) 0%, var(--card-dark-sheen) 45%, var(--card-dark) 100%);
    color: var(--paper);
  }
  .holder {
    position: absolute;
    left: 29px;
    top: 56px;
  }
  .holder__name {
    font-family: "Exo 2", sans-serif;
    font-style: italic;
    font-weight: 800;
    font-size: 15px;
    letter-spacing: 0.06em;
    text-transform: uppercase;
    line-height: 1;
  }
  .holder__title {
    margin-top: 4px;
    font-family: "EB Garamond", serif;
    font-size: 10px;
    color: var(--ink-soft);
  }
  .contacts {
    position: absolute;
    left: 22px;
    top: 217px;
    display: flex;
    align-items: center;
    list-style: none;
    font-family: "EB Garamond", serif;
    font-size: 9.5px;
    color: var(--ink);
  }
  .contacts__item {
    display: flex;
    align-items: center;
    gap: 5px;
    margin-right: 17px;
  }
  .contacts__icon {
    width: 16px;
    height: 16px;
    flex: none;
  }
  .brand {
    position: absolute;
    left: 0;
    right: 0;
    top: 118px;
    text-align: center;
    font-family: "EB Garamond", serif;
    font-weight: 500;
    font-size: 24px;
    letter-spacing: 0.14em;
    text-transform: uppercase;
    color: var(--paper);
    line-height: 1;
  }
</style>
</head>
<body>
<main class="stage">
  <section class="card card--front" aria-label="Business card front">
    <div class="holder">
      <p class="holder__name">Your Name</p>
      <p class="holder__title">Regional Security Officer (RSO)</p>
    </div>
    <ul class="contacts">
      <li class="contacts__item">
        <svg class="contacts__icon" viewBox="0 0 16 16" aria-hidden="true">
          <circle cx="8" cy="8" r="8" fill="var(--ink)"/>
          <path d="M5.3 4.2l1.4-.3.8 1.9-.9.7c.4 1 1.1 1.8 2 2.3l.8-.8 1.9.9-.4 1.4c-.2.4-.5.5-.9.5C7.2 10.6 5.1 8.4 4.9 5.2c0-.5.1-.9.4-1z" fill="var(--paper)"/>
        </svg>
        <span>123 456 7890</span>
      </li>
      <li class="contacts__item">
        <svg class="contacts__icon" viewBox="0 0 16 16" aria-hidden="true">
          <circle cx="8" cy="8" r="8" fill="var(--ink)"/>
          <circle cx="8" cy="8" r="4.6" fill="none" stroke="var(--paper)" stroke-width="0.9"/>
          <ellipse cx="8" cy="8" rx="2" ry="4.6" fill="none" stroke="var(--paper)" stroke-width="0.8"/>
          <line x1="3.4" y1="8" x2="12.6" y2="8" stroke="var(--paper)" stroke-width="0.8"/>
        </svg>
        <span>varnholtinsight.com</span>
      </li>
      <li class="contacts__item">
        <svg class="contacts__icon" viewBox="0 0 16 16" aria-hidden="true">
          <circle cx="8" cy="8" r="8" fill="var(--ink)"/>
          <rect x="4" y="5.2" width="8" height="5.6" rx="0.6" fill="var(--paper)"/>
          <path d="M4.3 5.6L8 8.4l3.7-2.8" fill="none" stroke="var(--ink)" stroke-width="0.8"/>
        </svg>
        <span>rso@varnholtinsight.com</span>
      </li>
    </ul>
  </section>

  <section class="card card--back" aria-label="Business card back">
    <p class="brand">Varnholt Insight</p>
  </section>
</main>
</body>
</html>
```